Business cards and stationary
Law Offices of Delphine R. Okonkwo
Professional
Delphine R. Okonkwo, Esq.
417 N. Cedar Brook Lane
Suite C-320
Plantation, Florida 33991
Delphine@Glenmorelegalcounsel.example
www.Glenmorelegalcounsel.example
The card should match my current website and logo. The back of the card should state: Practice Areas
Estate Planning
Probate and Trust Administration
Tax Law and Structuring
Business Structuring
Please no scales of justice or gavels

```html
<!DOCTYPE html>
<html lang="en">
<head>
<meta charset="utf-8">
<title>Law Offices of Delphine R. Okonkwo — Stationery</title>
<link href="https://fonts.googleapis.com/css2?family=Libre+Baskerville:wght@400;700&family=Open+Sans:wght@400;600&display=swap" rel="stylesheet">
<style>
  :root{
    --board:#8d8f92;
    --paper:#ffffff;
    --navy:#0b2f7a;
    --blue:#0b5bd3;
    --sky:#4aa3f0;
    --ink:#2b3a55;
    --faint:#e4ebf5;
    --label:#f2f2f2;
    --rule:#b9c3d2;
  }
  *{margin:0;padding:0;box-sizing:border-box}
  html,body{width:1200px;height:664px;overflow:hidden}
  body{background:var(--board);font-family:"Open Sans",sans-serif;color:var(--ink);position:relative}
  .piece{position:absolute;background:var(--paper);box-shadow:0 2px 6px rgba(0,0,0,.35);overflow:hidden}
  .label{position:absolute;font-size:7px;color:var(--label);text-align:center;font-family:"Open Sans",sans-serif}
  .wave{position:absolute;left:0;bottom:0;width:100%}
  .mark{display:flex;flex-direction:column;align-items:center;gap:2px}
  .mark .sq{width:14px;height:14px;background:var(--navy)}
  .mark .name{font-family:"Libre Baskerville",serif;font-size:5px;color:var(--navy);text-transform:uppercase;letter-spacing:.3px;text-align:center;line-height:1.2;white-space:nowrap}
  .faint-mark{position:absolute;left:50%;transform:translateX(-50%)}
  .faint-sq{width:90px;height:90px;background:var(--faint);margin:0 auto}
  .details{font-size:3.6px;line-height:1.45;color:var(--ink);white-space:nowrap}
  /* cards */
  .card{width:150px;height:67px;top:48px}
  .card-front{left:497px}
  .card-front .mark{position:absolute;left:8px;top:8px;align-items:flex-start}
  .card-front .mark .sq{width:11px;height:11px}
  .card-front .mark .name{font-size:3.8px;letter-spacing:0;text-align:left}
  .card-front .details{position:absolute;right:7px;top:8px;text-align:right;font-size:3.1px}
  .card-back{display:flex;flex-direction:column;align-items:center;justify-content:center;gap:3px;text-align:center}
  .card-back h4{font-family:"Libre Baskerville",serif;font-size:5px;font-weight:700}
  .card-back ul{list-style:none;font-size:3.8px;line-height:1.4}
  .back-1{left:662px;color:var(--navy)}
  .back-1 h4{color:var(--navy)}
  .back-2{left:826px;background:linear-gradient(135deg,var(--navy),var(--blue) 60%,var(--sky));color:#fff}
  .back-3{left:991px;width:142px;background:linear-gradient(135deg,var(--navy),var(--blue));color:#fff;border:3px solid #fff;outline:1px solid var(--blue)}
  /* sheets */
  .sheet{width:331px;height:489px;top:149px}
  .fax{left:29px}
  .letterhead{left:396px}
  .sheet .mark{position:absolute;top:16px;left:50%;transform:translateX(-50%)}
  .fax-title{position:absolute;right:14px;top:56px;font-size:6px;font-weight:600;color:var(--ink)}
  .fax-table{position:absolute;left:14px;top:66px;border-collapse:collapse;font-size:4px;width:303px}
  .fax-table td{border:1px solid var(--rule);height:11px;padding:0 3px}
  .fax-table td.k{width:24px;background:#f3f6fa}
  .fax-checks{position:absolute;left:14px;top:124px;display:flex;gap:20px;font-size:4px;white-space:nowrap}
  .fax-checks span::before{content:"";display:inline-block;width:4px;height:4px;border:1px solid var(--ink);margin-right:2px;vertical-align:middle}
  .footer{position:absolute;right:12px;bottom:6px;font-size:3.4px;color:#fff;text-align:right;line-height:1.4;white-space:nowrap}
  /* envelopes */
  .env-front{left:758px;top:149px;width:413px;height:177px}
  .env-front .mark{position:absolute;left:16px;top:12px;align-items:flex-start}
  .env-front .mark .name{text-align:left}
  .env-front .details{position:absolute;left:16px;top:46px}
  .env-back{width:409px;height:168px}
  .env-back-1{left:763px;top:348px}
  .env-back-2{left:792px;top:456px;width:379px;height:180px}
  .env-back-2 .mark{position:absolute;left:50%;top:34px;transform:translateX(-50%)}
</style>
</head>
<body>

<div class="label" style="left:497px;top:30px;width:150px">Business Card (Front)</div>
<div class="label" style="left:662px;top:30px;width:150px">Business Card Back - Option 1</div>
<div class="label" style="left:826px;top:30px;width:150px">Business Card Back - Option 2</div>
<div class="label" style="left:991px;top:30px;width:142px">Business Card Back - Option 3</div>
<div class="label" style="left:29px;top:136px;width:331px">Fax Cover</div>
<div class="label" style="left:396px;top:136px;width:331px">Letterhead</div>
<div class="label" style="left:758px;top:136px;width:413px">Envelope (Front)</div>
<div class="label" style="left:763px;top:336px;width:409px">Envelope Back - Option 1</div>
<div class="label" style="left:792px;top:443px;width:379px">Envelope Back - Option 2</div>

<svg width="0" height="0" style="position:absolute">
  <defs>
    <linearGradient id="deep" x1="0" x2="1"><stop offset="0" stop-color="#0b2f7a"/><stop offset="1" stop-color="#0b5bd3"/></linearGradient>
    <linearGradient id="light" x1="0" x2="1"><stop offset="0" stop-color="#4aa3f0"/><stop offset="1" stop-color="#0b5bd3"/></linearGradient>
  </defs>
</svg>

<!-- Business card front -->
<div class="piece card card-front">
  <div class="mark"><div class="sq"></div><div class="name">Law Offices of<br>Delphine R. Okonkwo</div></div>
  <div class="details">Delphine R. Okonkwo, Esq.<br>417 N. Cedar Brook Lane<br>Suite C-320<br>Plantation, Florida 33991<br>Delphine@Glenmorelegalcounsel.example<br>www.Glenmorelegalcounsel.example</div>
  <svg class="wave" viewBox="0 0 150 24" preserveAspectRatio="none" height="24">
    <path d="M0 10 C40 0 90 26 150 6 L150 24 L0 24Z" fill="url(#light)"/>
    <path d="M0 16 C45 6 95 28 150 12 L150 24 L0 24Z" fill="url(#deep)"/>
  </svg>
</div>

<div class="piece card card-back back-1">
  <h4>Practice Areas</h4>
  <ul><li>Estate Planning</li><li>Probate and Trust Administration</li><li>Tax Law and Structuring</li><li>Business Structuring</li></ul>
  <svg class="wave" viewBox="0 0 150 10" preserveAspectRatio="none" height="10"><path d="M0 6 C50 0 100 10 150 3 L150 10 L0 10Z" fill="url(#deep)"/></svg>
</div>
<div class="piece card card-back back-2">
  <h4>Practice Areas</h4>
  <ul><li>Estate Planning</li><li>Probate and Trust Administration</li><li>Tax Law and Structuring</li><li>Business Structuring</li></ul>
</div>
<div class="piece card card-back back-3">
  <h4>Practice Areas</h4>
  <ul><li>Estate Planning</li><li>Probate and Trust Administration</li><li>Tax Law and Structuring</li><li>Business Structuring</li></ul>
</div>

<!-- Fax cover -->
<div class="piece sheet fax">
  <div class="mark"><div class="sq"></div><div class="name">Law Offices of<br>Delphine R. Okonkwo</div></div>
  <div class="fax-title">FAX</div>
  <table class="fax-table">
    <tr><td class="k">To:</td><td></td><td class="k">Phone:</td><td></td></tr>
    <tr><td class="k">Date:</td><td></td><td class="k">Pages:</td><td></td></tr>
    <tr><td class="k">From:</td><td></td><td class="k">Fax:</td><td></td></tr>
    <tr><td class="k">Re:</td><td></td><td class="k">CC:</td><td></td></tr>
  </table>
  <div class="fax-checks"><span>Urgent</span><span>For Review</span><span>Please Comment</span><span>Please Reply</span><span>Please Recycle</span></div>
  <div class="faint-mark" style="top:200px"><div class="faint-sq"></div></div>
  <svg class="wave" viewBox="0 0 331 70" preserveAspectRatio="none" height="70">
    <path d="M0 30 C90 0 200 60 331 14 L331 70 L0 70Z" fill="url(#light)"/>
    <path d="M0 44 C100 14 210 70 331 30 L331 70 L0 70Z" fill="url(#deep)"/>
  </svg>
  <div class="footer">417 N. Cedar Brook Lane, Suite C-320 · Plantation, Florida 33991<br>www.Glenmorelegalcounsel.example</div>
</div>

<!-- Letterhead -->
<div class="piece sheet letterhead">
  <div class="mark"><div class="sq"></div><div class="name">Law Offices of<br>Delphine R. Okonkwo</div></div>
  <div class="faint-mark" style="top:130px"><div class="faint-sq"></div></div>
  <svg class="wave" viewBox="0 0 331 70" preserveAspectRatio="none" height="70">
    <path d="M0 30 C90 0 200 60 331 14 L331 70 L0 70Z" fill="url(#light)"/>
    <path d="M0 44 C100 14 210 70 331 30 L331 70 L0 70Z" fill="url(#deep)"/>
  </svg>
  <div class="footer">417 N. Cedar Brook Lane, Suite C-320 · Plantation, Florida 33991<br>www.Glenmorelegalcounsel.example</div>
</div>

<!-- Envelope front -->
<div class="piece env-front">
  <div class="mark"><div class="sq"></div><div class="name">Law Offices of<br>Delphine R. Okonkwo</div></div>
  <div class="details">417 N. Cedar Brook Lane<br>Suite C-320<br>Plantation, Florida 33991</div>
  <svg class="wave" viewBox="0 0 413 40" preserveAspectRatio="none" height="40">
    <path d="M0 20 C120 0 260 40 413 8 L413 40 L0 40Z" fill="url(#light)"/>
    <path d="M0 28 C130 8 270 44 413 18 L413 40 L0 40Z" fill="url(#deep)"/>
  </svg>
</div>

<!-- Envelope back option 1 -->
<div class="piece env-back env-back-1">
  <svg viewBox="0 0 409 168" width="409" height="168" preserveAspectRatio="none">
    <path d="M0 0 L409 0 L220 72 Q204 78 188 72 Z" fill="#f4f6f9" stroke="#c8d0dc"/>
    <path d="M0 0 L188 72 Q204 78 220 72 L409 0" fill="none" stroke="url(#deep)" stroke-width="3"/>
  </svg>
</div>

<!-- Envelope back option 2 -->
<div class="piece env-back env-back-2">
  <svg viewBox="0 0 379 180" width="379" height="180" preserveAspectRatio="none" style="position:absolute;left:0;top:0">
    <path d="M0 0 L379 0 L205 78 Q189 85 173 78 Z" fill="url(#deep)"/>
    <path d="M0 0 L173 78 Q189 85 205 78 L379 0" fill="none" stroke="url(#light)" stroke-width="4"/>
  </svg>
  <div class="mark"><div class="sq" style="background:#fff"></div><div class="name" style="color:#fff">Law Offices of<br>Delphine R. Okonkwo</div></div>
</div>

</body>
</html>
```